Plakat/Handzettel für Bildungs- und Gesundheitsservice
Zielgruppe
Wir benötigen eine Datei, die wir als
a.) Handzettel (DIN A4) sowie
b.) als Poster (DIN A1) ausdrucken können.
ACHTUNG:
a.) bitte in einem Format liefern, in dem den CODE XXXX immer 'selbst' austauschen können. Handzettel kann als Word-Datei.. das Poster lieber in einem Format, was mit Photoshop ggf. aufrufbar ist (weil wir den Code auf jedem Poster ändern müssen)
b.) Anliegend der Text der auf das Poster und Handzettel muss.
Aufgabenstellung
siehe Farben Website www.lindquel-akadem.com
bitte selbst entscheiden, ob Fotos auf dem Poster bzw. Handzettel sein sollen.

```html
<!DOCTYPE html>
<html lang="de">
<head>
<meta charset="utf-8">
<title>Lindquel Akadem – Plakat</title>
<link rel="stylesheet" href="https://fonts.googleapis.com/css2?family=Bebas+Neue&family=Montserrat:wght@400;600;700&family=Cinzel:wght@500&display=swap">
<style>
  :root {
    --teal-dark: #24637d;
    --teal-mid: #2e7d97;
    --teal-light: #47b5d1;
    --sky: #cfe9f7;
    --text-gray: #3b4650;
    --white: #ffffff;
    --stage: #e6ecee;
  }
  * { margin: 0; padding: 0; box-sizing: border-box; }
  html, body { width: 1200px; height: 1177px; overflow: hidden; background: var(--stage); }
  .poster {
    position: absolute; left: 183px; top: 0; width: 834px; height: 1177px;
    overflow: hidden;
    background: linear-gradient(180deg, #ffffff 0%, #f4fafd 55%, var(--sky) 100%);
    font-family: "Montserrat", sans-serif; color: var(--text-gray);
  }
  .hero-photo {
    position: absolute; left: 0; top: 0; width: 834px; height: 645px;
    background: linear-gradient(120deg, #eef7fa 0%, #cfe6ec 45%, #9fc3cf 70%, #2a3a44 100%);
  }
  .hero-fade {
    position: absolute; left: 0; top: 565px; width: 834px; height: 90px;
    background: linear-gradient(180deg, rgba(244,250,253,0) 0%, #f4fafd 100%);
  }
  .brand-dot {
    position: absolute; left: 231px; top: 60px; width: 40px; height: 40px;
    border-radius: 50%; background: var(--teal-dark);
  }
  .brand {
    position: absolute; left: 110px; top: 148px; width: 284px;
    text-align: center; font-family: "Cinzel", serif; font-weight: 500;
    font-size: 19px; letter-spacing: 4px; color: #1b1b1b;
  }
  .card {
    position: absolute; left: 38px; top: 194px; width: 428px; height: 983px;
    border-radius: 14px 14px 0 0;
    background: linear-gradient(180deg, #ffffff 0%, #ffffff 55%, rgba(255,255,255,0) 100%);
  }
  .condensed { display: inline-block; white-space: nowrap; transform-origin: left top; }
  .headline { font-family: "Bebas Neue", sans-serif; font-weight: 400; }
  .headline .line-1 {
    position: absolute; left: 70px; top: 221px; font-size: 113px; line-height: 1;
    color: var(--teal-dark);
  }
  .headline .line-2 {
    position: absolute; left: 68px; top: 307px; font-size: 148px; line-height: 1;
    color: var(--teal-light);
  }
  .subhead {
    position: absolute; left: 72px; top: 439px;
    font-family: "Bebas Neue", sans-serif; font-size: 37px; line-height: 33px;
    color: var(--teal-dark); transform: scaleX(0.86);
  }
  .timeline {
    position: absolute; left: 107px; top: 600px; width: 4px; height: 312px;
    background: var(--teal-light);
  }
  .hex { position: absolute; left: 74px; width: 70px; height: 77px; }
  .section-title {
    position: absolute; left: 169px;
    font-family: "Bebas Neue", sans-serif; font-weight: 400; font-size: 34px;
    line-height: 1; color: var(--teal-light); transform: scaleX(0.92);
  }
  .section-note {
    position: absolute; left: 169px; top: 567px; font-size: 11.5px; line-height: 14px;
  }
  .topic-list { position: absolute; left: 171px; list-style: none; }
  .topic-list li {
    position: relative; padding-left: 30px; font-size: 15px; font-weight: 600;
    line-height: 23.5px; white-space: nowrap;
  }
  .topic-list li::before {
    content: ""; position: absolute; left: 0; top: 6px; width: 12px; height: 12px;
    border-radius: 50%; background: var(--teal-dark);
  }
  .topic-list li::after {
    content: ""; position: absolute; left: 3px; top: 9px; width: 5px; height: 3px;
    border-left: 2px solid var(--white); border-bottom: 2px solid var(--white);
    transform: rotate(-45deg);
  }
  .couple-photo {
    position: absolute; left: 470px; top: 945px; width: 330px; height: 232px;
    border-radius: 130px 130px 0 0;
    background: linear-gradient(160deg, #d9b89c 0%, #8a96a4 45%, #3a4a5c 100%);
  }
  .code-box {
    position: absolute; left: 486px; top: 653px; width: 284px; height: 319px;
    border-radius: 10px;
    background: linear-gradient(180deg, var(--teal-mid) 0%, var(--teal-dark) 100%);
    box-shadow: 0 5px 0 var(--teal-light);
    text-align: center; color: var(--white);
  }
  .code-box h3 {
    margin-top: 22px; font-family: "Bebas Neue", sans-serif; font-weight: 400;
    font-size: 33px; line-height: 32.5px;
  }
  .code-box .intro { margin-top: 6px; font-size: 15.5px; font-weight: 600; line-height: 21px; }
  .code-pill {
    margin: 10px auto 0; width: 238px; height: 31px; border-radius: 16px;
    background: var(--teal-light); box-shadow: 0 3px 0 #1c4f64;
    font-weight: 700; font-size: 17px; line-height: 31px; letter-spacing: 8px;
  }
  .code-box .register { margin-top: 14px; font-size: 15.5px; font-weight: 600; line-height: 21px; }
  .code-box .portal { font-size: 15.5px; font-weight: 700; color: var(--teal-light); line-height: 21px; }
  .statement {
    position: absolute; left: 73px; top: 1040px;
    font-family: "Bebas Neue", sans-serif; font-size: 21px; line-height: 22px;
    color: var(--teal-dark); transform: scaleX(0.84);
  }
  .url-band {
    position: absolute; left: 0; top: 1112px; width: 474px; height: 56px;
    background: linear-gradient(90deg, var(--teal-light) 0%, var(--teal-dark) 100%);
    clip-path: polygon(44px 0, 100% 0, 100% 100%, 0 100%, 0 49px, 30px 49px);
  }
  .url-band span {
    position: absolute; left: 73px; top: 16px; font-weight: 700; font-size: 18.5px;
    color: var(--white); letter-spacing: 0.5px; white-space: nowrap;
  }
</style>
</head>
<body>
<main class="poster">
  <div class="hero-photo" role="img" aria-label="Foto: lächelnde Dozentin mit Brille am Rednerpult in einem hellen Hörsaal"></div>
  <div class="hero-fade"></div>

  <div class="brand-dot"></div>
  <div class="brand">LINDQUEL AKADEM</div>

  <div class="card"></div>

  <h1 class="headline"><span class="line-1">LINDQUEL</span><span class="line-2">AKADEM</span></h1>
  <p class="subhead condensed">HUNDERTE VON ABENDLICHEN<br>UNIVERSITÄREN LIVE-VERANSTALTUNGEN</p>

  <div class="timeline"></div>

  <svg class="hex" style="top:528px" viewBox="0 0 72 80" aria-hidden="true">
    <polygon points="36,2 70,21 70,59 36,78 2,59 2,21" fill="var(--teal-dark)" stroke="var(--teal-light)" stroke-width="3"/>
    <rect x="22" y="22" width="28" height="18" rx="2" fill="none" stroke="#fff" stroke-width="2"/>
    <circle cx="36" cy="30" r="3" fill="none" stroke="#fff" stroke-width="1.6"/>
    <g fill="none" stroke="#fff" stroke-width="1.6">
      <circle cx="25" cy="47" r="2.5"/><circle cx="33" cy="47" r="2.5"/><circle cx="41" cy="47" r="2.5"/><circle cx="49" cy="47" r="2.5"/>
      <path d="M21 56 q4 -6 8 0 M29 56 q4 -6 8 0 M37 56 q4 -6 8 0 M45 56 q4 -6 8 0"/>
    </g>
  </svg>
  <svg class="hex" style="top:776px" viewBox="0 0 72 80" aria-hidden="true">
    <polygon points="36,2 70,21 70,59 36,78 2,59 2,21" fill="var(--teal-dark)" stroke="var(--teal-light)" stroke-width="3"/>
    <rect x="15" y="30" width="42" height="24" rx="2" fill="none" stroke="#fff" stroke-width="2"/>
    <path d="M30 58 h12 M36 54 v4" stroke="#fff" stroke-width="2"/>
    <circle cx="48" cy="25" r="7" fill="var(--teal-dark)" stroke="#fff" stroke-width="1.6"/>
    <g fill="none" stroke="#fff" stroke-width="1.4">
      <circle cx="24" cy="37" r="2"/><circle cx="36" cy="37" r="2"/><circle cx="48" cy="37" r="2"/>
      <circle cx="24" cy="46" r="2"/><circle cx="36" cy="46" r="2"/><circle cx="48" cy="46" r="2"/>
    </g>
  </svg>
  <svg class="hex" style="top:910px" viewBox="0 0 72 80" aria-hidden="true">
    <polygon points="36,2 70,21 70,59 36,78 2,59 2,21" fill="var(--teal-dark)" stroke="var(--teal-light)" stroke-width="3"/>
    <path d="M16 24 h30 v18 h-20 l-7 6 v-6 h-3 z" fill="none" stroke="#fff" stroke-width="2"/>
    <path d="M46 32 h10 v18 h-3 v6 l-7 -6 h-16 v-8" fill="none" stroke="#fff" stroke-width="2"/>
    <path d="M21 31 h20 M21 36 h14" stroke="#fff" stroke-width="1.6"/>
  </svg>

  <h2 class="section-title condensed" style="top:532px">LIVE-VORLESUNGEN</h2>
  <p class="section-note">von 150 Professorinnen und Professoren<br>(mit Zertifikat der Teilnahme)</p>
  <ul class="topic-list" style="top:600px">
    <li>Gesundheit</li>
    <li>Psychologie</li>
    <li>Medizin</li>
    <li>Marketing</li>
    <li>Führung</li>
    <li>und viele weitere Themen</li>
  </ul>

  <h2 class="section-title condensed" style="top:770px">LIVE-PRAKTISCHE SEMINARE</h2>
  <ul class="topic-list" style="top:803px">
    <li>Prävention von Burnout</li>
    <li>Resilienz Training</li>
    <li>Und viele weitere Themen</li>
  </ul>

  <h2 class="section-title condensed" style="top:904px">LIVE-DIALOGRUNDEN</h2>
  <ul class="topic-list" style="top:939px">
    <li>Beratung zu Erziehungsfragen</li>
    <li>Umgang mit Trauer</li>
    <li>Und viele weitere Themen</li>
  </ul>

  <div class="couple-photo" role="img" aria-label="Foto: Paar sitzt gemeinsam vor einem Laptop"></div>

  <aside class="code-box">
    <h3><span class="condensed" style="transform:scaleX(0.92);transform-origin:center top">ZUGANG ZUM VIRTUELLEN<br>HÖRSAAL AUF DEM<br>LINDQUEL AKADEM</span></h3>
    <p class="intro">Ihr Code für eine<br>kostenfreie Nutzung:</p>
    <div class="code-pill">CODE XXXX</div>
    <p class="register">Melden Sie sich an:</p>
    <p class="portal">https://portal.lindquel<br>akadem.com/register</p>
  </aside>

  <p class="statement condensed">WIR ÖFFNEN DIE TÜREN ZUM VIRTUELLEN HÖRSAAL FÜR „ALLE“ MITARBEITENDE,<br>DENN BEI UNS IST WISSENSCHAFTLICHE BILDUNG FÜR ALLE DA.</p>

  <div class="url-band"><span>WWW.LINDQUEL-AKADEM.COM</span></div>
</main>
</body>
</html>
```